Darrowby's Insurance Servives, Inc.

Full Service Insurance Broker.
Senior Health Care, Life, Annuity, Auto and Home
Specializing in Brovanta Supplements. No cost, No Obligation Consulting.

Target Market(s)

General Public and senior citizens

Industry/Entity Type

Insurance Broker

Font styles to use
Decorative
Script

```html
<!DOCTYPE html>
<html lang="en">
<head>
<meta charset="UTF-8">
<title>Darrowby's Insurance Servives, Inc.</title>
<link href="https://fonts.googleapis.com/css2?family=Yellowtail&family=Montserrat:ital,wght@0,300;0,800;1,800&family=Saira+Condensed:wght@600&display=swap" rel="stylesheet">
<style>
  :root {
    --white: #ffffff;
    --yellow: #fdb515;
    --orange: #fb8c00;
    --black: #1f1f1f;
    --green: #7ac943;
    --teal-light: #8fd6c6;
    --teal-dark: #3fae98;
    --tick-grey: #8a8a8a;
  }
  html, body {
    margin: 0;
    padding: 0;
    width: 1200px;
    height: 1200px;
    overflow: hidden;
    background: var(--white);
  }
  .flyer {
    position: relative;
    width: 1200px;
    height: 1200px;
    overflow: hidden;
    background: var(--white);
  }
  .flyer-shapes {
    position: absolute;
    inset: 0;
    width: 1200px;
    height: 1200px;
  }
  .brand-name {
    position: absolute;
    left: 100px;
    top: 205px;
    width: 500px;
    text-align: center;
    margin: 0;
    font-family: 'Yellowtail', cursive;
    font-weight: 400;
    font-size: 112px;
    line-height: 1;
    color: var(--black);
  }
  .brand-sub {
    position: absolute;
    left: 100px;
    top: 372px;
    width: 500px;
    text-align: center;
    margin: 0;
    font-family: 'Montserrat', sans-serif;
    font-weight: 800;
    font-size: 29px;
    color: var(--black);
    letter-spacing: 0.3px;
  }
  .service-list {
    position: absolute;
    left: 28px;
    top: 552px;
    margin: 0;
    padding: 0;
    list-style: none;
    font-family: 'Saira Condensed', sans-serif;
    font-weight: 600;
    font-style: italic;
    font-size: 33px;
    line-height: 46px;
    color: var(--black);
  }
  .service-list li {
    position: relative;
    padding-left: 36px;
  }
  .service-list .tick {
    position: absolute;
    left: 0;
    top: 11px;
    width: 24px;
    height: 24px;
  }
  .specialty {
    position: absolute;
    left: 238px;
    top: 792px;
    margin: 0;
    font-family: 'Saira Condensed', sans-serif;
    font-weight: 600;
    font-style: italic;
    font-size: 44px;
    line-height: 53px;
    color: var(--black);
  }
  .consult-bar {
    position: absolute;
    left: 70px;
    top: 977px;
    width: 570px;
    height: 51px;
    background: var(--black);
    display: flex;
    align-items: center;
    justify-content: center;
    margin: 0;
    font-family: 'Saira Condensed', sans-serif;
    font-weight: 600;
    font-style: italic;
    font-size: 33px;
    color: var(--orange);
  }
  .broker-badge {
    position: absolute;
    left: 862px;
    top: 730px;
    width: 300px;
    height: 300px;
    border-radius: 50%;
    background: var(--black);
    color: var(--white);
    font-family: 'Montserrat', sans-serif;
  }
  .broker-badge .line {
    position: absolute;
    left: 36px;
    margin: 0;
    white-space: nowrap;
  }
  .broker-badge .line-light {
    top: 8px;
    font-weight: 300;
    font-size: 35px;
    top: 12px;
    margin-top: 0;
    transform: translateY(0);
    top: 10px;
  }
  .broker-badge .line-light { top: 10px; }
  .broker-badge .line-bold {
    font-weight: 800;
    font-style: italic;
    font-size: 42px;
  }
  .broker-badge .line-1 { top: 8px; left: 42px; }
  .broker-badge .line-2 { top: 68px; left: 36px; }
  .broker-badge .line-3 { top: 118px; left: 36px; color: var(--green); }
  .broker-badge .lines { position: absolute; left: 0; top: 12px; width: 300px; height: 200px; }
</style>
</head>
<body>
<main class="flyer">
  <svg class="flyer-shapes" viewBox="0 0 1500 1500" xmlns="http://www.w3.org/2000/svg">
    <defs>
      <linearGradient id="scrubs-tone" x1="0" y1="0" x2="1" y2="1">
        <stop offset="0" stop-color="var(--teal-dark)"/>
        <stop offset="0.5" stop-color="var(--teal-light)"/>
        <stop offset="1" stop-color="var(--teal-dark)"/>
      </linearGradient>
    </defs>
    <rect class="band-base" x="0" y="215" width="1500" height="1070" fill="var(--orange)"/>
    <polygon class="band-white" points="0,420 865,1285 0,1285" fill="var(--white)"/>
    <polygon class="band-white-right" points="1055,1285 1500,840 1500,1285" fill="var(--white)"/>
    <polygon class="panel-yellow" points="0,215 833,215 955,337 445,800 0,355" fill="var(--yellow)"/>
    <polygon class="panel-left-orange" points="0,468 410,878 0,1288" fill="var(--orange)"/>
    <polygon class="frame-black" points="1090,215 1500,215 1500,720 935,1285 445,800" fill="var(--black)"/>
    <polygon class="photo-area" role="img" aria-label="Photo: gloved hands of a doctor in teal scrubs with a stethoscope, holding coins and a banknote"
             points="545,770 1100,215 1500,215 1500,705 990,1215" fill="url(#scrubs-tone)"/>
    <polygon class="accent-orange-right" points="1000,1285 1055,1285 1445,895 1415,865" fill="var(--orange)"/>
  </svg>

  <h1 class="brand-name">Darrowby's</h1>
  <p class="brand-sub">Insurance Servives, Inc</p>

  <ul class="service-list">
    <li><svg class="tick" viewBox="0 0 24 24"><rect x="1" y="1" width="22" height="22" rx="5" fill="var(--tick-grey)"/><path d="M6 12.5l4 4 8-9" fill="none" stroke="var(--white)" stroke-width="3" stroke-linecap="round" stroke-linejoin="round"/></svg>Senior<br>Health Care,</li>
    <li><svg class="tick" viewBox="0 0 24 24"><rect x="1" y="1" width="22" height="22" rx="5" fill="var(--tick-grey)"/><path d="M6 12.5l4 4 8-9" fill="none" stroke="var(--white)" stroke-width="3" stroke-linecap="round" stroke-linejoin="round"/></svg>Life,</li>
    <li><svg class="tick" viewBox="0 0 24 24"><rect x="1" y="1" width="22" height="22" rx="5" fill="var(--tick-grey)"/><path d="M6 12.5l4 4 8-9" fill="none" stroke="var(--white)" stroke-width="3" stroke-linecap="round" stroke-linejoin="round"/></svg>Annuity,</li>
    <li><svg class="tick" viewBox="0 0 24 24"><rect x="1" y="1" width="22" height="22" rx="5" fill="var(--tick-grey)"/><path d="M6 12.5l4 4 8-9" fill="none" stroke="var(--white)" stroke-width="3" stroke-linecap="round" stroke-linejoin="round"/></svg>Auto and<br>Home</li>
  </ul>

  <p class="specialty">Specializing<br>in Brovanta<br>Supplements</p>

  <p class="consult-bar">No cost, No Obligation Consulting.</p>

  <div class="broker-badge">
    <div class="lines">
      <p class="line line-light line-1" style="top:40px;">Full Service</p>
      <p class="line line-bold line-2" style="top:96px;">Insurance</p>
      <p class="line line-bold line-3" style="top:148px;">Broker.</p>
    </div>
  </div>
</main>
</body>
</html>
```